Memento Mori Calendar

I’m looking for a graphic designer to create a Memento Mori–style life calendar that captures the essence of QUILNEXA — minimal, timeless, and deeply philosophical.

The design should be black and white only, with a refined, clean aesthetic and a sense of stillness and precision.
It should feel modern yet eternal, reflecting the themes of time, mortality, and presence.

Deliverables (Print-Ready Files):

24 x 30 in

24 x 32 in

24 x 36 in

A1 (594 x 841 mm)

All formats should be high-resolution and ready for professional printing (300 DPI, CMYK).

Design Requirements:

The calendar layout should follow the Memento Mori life calendar concept (weeks of life represented as small squares or circles).

The overall tone: minimal, meditative, monochrome.

Include the brand name: QUILNEXA (in an elegant, understated placement).

Add the following quote at the bottom or in a subtle position:

“Life can only be understood backwards; but it must be lived forwards.”
— Anselm Brodtvik

Target Market(s)

The QUILNEXA audience consists of urban, creative individuals aged 25 to 45, belonging to a middle to upper-middle income class. They lead conscious, quietly ambitious lives, seeking balance between inner depth and modern design. Their values center on awareness, presence, authenticity, and emotional depth, reflected in their preference for a monochrome, minimal, and timeless aesthetic. They tend to be introverted, reflective, and spiritually curious, drawn to brands that embody meaning and restraint rather than excess. Their cultural and stylistic affinities include Vinth, Polde, Ro Sefi, The Garden of Hours, Dussant, and Varolé — labels that share QUILNEXAs devotion to simplicity, substance, and subtle ritual.

Font styles to use
Serif
Sans Serif

Colors

Designer to choose only greyscale colors for use in the design.

Requirements
Must have
• The calendar layout should follow the Memento Mori life calendar concept (weeks of life represented as small squares or circles). The overall tone: minimal, meditative, monochrome. Include the brand name: trvolquen (in an elegant, understated placement). Add the following quote at the bottom or in a subtle position: “Life can only be understood backwards; but it must be lived forwards.” — Anselm Brodtvik

```html
<!DOCTYPE html>
<html lang="en">
<head>
<meta charset="utf-8">
<title>Tempora Nostra — Life Calendar</title>
<link rel="stylesheet" href="https://fonts.googleapis.com/css2?family=Montserrat:wght@400;500;600;700&family=Tinos:ital,wght@0,700;1,400&display=swap">
<style>
  :root {
    --backdrop: #e6e6e7;
    --paper: #fefefe;
    --ink: #070707;
    --ink-soft: #333333;
    --cell-line: #5a5a5a;
    --label: #2a2a2a;
    --inverse: #ffffff;
  }
  * { box-sizing: border-box; margin: 0; padding: 0; }
  html, body {
    width: 1015px; height: 1200px; overflow: hidden;
    background: var(--backdrop);
  }
  .poster {
    position: absolute; left: 27.5px; top: 0;
    width: 960px; height: 1200px;
    background: var(--paper);
    font-family: "Montserrat", sans-serif;
    color: var(--ink);
  }
  .title-band {
    position: absolute; left: 18px; top: 12px;
    width: 141px; height: 1174px;
    background: var(--ink);
    overflow: hidden;
  }
  .title-band__text {
    position: absolute; left: 63px; top: 50%;
    transform: translate(-50%, -50%) rotate(-90deg);
    white-space: nowrap;
    font-weight: 600; font-size: 104px; line-height: 1;
    color: var(--inverse);
  }
  .title-band__axis {
    position: absolute; left: 132px; top: 43px;
    transform: translate(-50%, -50%) rotate(-90deg);
    font-weight: 700; font-size: 8px; color: var(--inverse);
  }
  .brand {
    position: absolute; left: 480px; top: 8px;
    transform: translateX(-50%);
    font-weight: 700; font-size: 33px; letter-spacing: 0.3px;
    color: var(--ink-soft);
  }
  .calendar { position: absolute; left: 0; top: 0; width: 960px; height: 1200px; }
  .calendar .axis-title { font: 700 10px "Montserrat", sans-serif; fill: var(--ink); }
  .calendar .week-no { font: 500 4.6px "Montserrat", sans-serif; fill: var(--label); text-anchor: middle; }
  .calendar .week-no--major { font: 700 9.5px "Montserrat", sans-serif; fill: var(--ink); }
  .calendar .year-no { font: 500 4.6px "Montserrat", sans-serif; fill: var(--label); text-anchor: middle; }
  .calendar .year-no--major { font: 700 10px "Montserrat", sans-serif; fill: var(--ink); }
  .quote {
    position: absolute; left: 556px; top: 1133px;
    transform: translateX(-50%);
    white-space: nowrap;
    font-family: "Tinos", serif; font-weight: 700; font-size: 18.5px;
    color: var(--ink-soft);
  }
  .quote__author {
    position: absolute; right: 85px; top: 1157px;
    font-family: "Tinos", serif; font-style: italic; font-size: 18.5px;
    color: var(--ink-soft);
  }
</style>
</head>
<body>
<main class="poster">
  <div class="title-band">
    <span class="title-band__text">TEMPORA NOSTRA</span>
    <span class="title-band__axis">Years</span>
  </div>

  <div class="brand">TRVOLQUEN</div>

  <svg class="calendar" viewBox="0 0 960 1200" width="960" height="1200" aria-label="Life calendar: 80 years of 52 weeks">
    <defs>
      <pattern id="week-cell" patternUnits="userSpaceOnUse" x="226" y="-4" width="12.35" height="12.2">
        <rect x="0.4" y="0.4" width="7.8" height="7.8" fill="none" stroke="var(--cell-line)" stroke-width="0.7"/>
      </pattern>
    </defs>

    <text class="axis-title" x="229" y="42">Week</text>

    <g class="week-header" transform="translate(0,61)">
      <text class="week-no" x="230">1</text><text class="week-no" x="242.35">2</text><text class="week-no" x="254.7">3</text><text class="week-no" x="267.05">4</text><text class="week-no week-no--major" x="279.4" y="1.5">5</text><text class="week-no" x="291.75">6</text><text class="week-no" x="304.1">7</text><text class="week-no" x="316.45">8</text><text class="week-no" x="328.8">9</text><text class="week-no week-no--major" x="341.15" y="1.5">10</text><text class="week-no" x="353.5">11</text><text class="week-no" x="365.85">12</text><text class="week-no" x="378.2">13</text><text class="week-no" x="390.55">14</text><text class="week-no week-no--major" x="402.9" y="1.5">15</text><text class="week-no" x="415.25">16</text><text class="week-no" x="427.6">17</text><text class="week-no" x="439.95">18</text><text class="week-no" x="452.3">19</text><text class="week-no week-no--major" x="464.65" y="1.5">20</text><text class="week-no" x="477">21</text><text class="week-no" x="489.35">22</text><text class="week-no" x="501.7">23</text><text class="week-no" x="514.05">24</text><text class="week-no week-no--major" x="526.4" y="1.5">25</text><text class="week-no" x="538.75">26</text>
      <text class="week-no" x="575.8">27</text><text class="week-no" x="588.15">28</text><text class="week-no" x="600.5">29</text><text class="week-no week-no--major" x="612.85" y="1.5">30</text><text class="week-no" x="625.2">31</text><text class="week-no" x="637.55">32</text><text class="week-no" x="649.9">33</text><text class="week-no" x="662.25">34</text><text class="week-no week-no--major" x="674.6" y="1.5">35</text><text class="week-no" x="686.95">36</text><text class="week-no" x="699.3">37</text><text class="week-no" x="711.65">38</text><text class="week-no" x="724">39</text><text class="week-no week-no--major" x="736.35" y="1.5">40</text><text class="week-no" x="748.7">41</text><text class="week-no" x="761.05">42</text><text class="week-no" x="773.4">43</text><text class="week-no" x="785.75">44</text><text class="week-no week-no--major" x="798.1" y="1.5">45</text><text class="week-no" x="810.45">46</text><text class="week-no" x="822.8">47</text><text class="week-no" x="835.15">48</text><text class="week-no" x="847.5">49</text><text class="week-no week-no--major" x="859.85" y="1.5">50</text><text class="week-no" x="872.2">51</text><text class="week-no" x="884.55">52</text>
    </g>

    <g class="decade" transform="translate(0,67)">
      <rect x="226" y="-4" width="321.1" height="122" fill="url(#week-cell)"/><rect x="571.8" y="-4" width="321.1" height="122" fill="url(#week-cell)"/>
      <text class="year-no" x="211" y="1.6">1</text><text class="year-no" x="211" y="13.8">2</text><text class="year-no" x="211" y="26">3</text><text class="year-no" x="211" y="38.2">4</text><text class="year-no" x="211" y="50.4">5</text><text class="year-no" x="211" y="62.6">6</text><text class="year-no" x="211" y="74.8">7</text><text class="year-no" x="211" y="87">8</text><text class="year-no" x="211" y="99.2">9</text><text class="year-no year-no--major" x="211" y="113.3">10</text>
    </g>
    <g class="decade" transform="translate(0,201.4)">
      <rect x="226" y="-4" width="321.1" height="122" fill="url(#week-cell)"/><rect x="571.8" y="-4" width="321.1" height="122" fill="url(#week-cell)"/>
      <text class="year-no" x="211" y="1.6">11</text><text class="year-no" x="211" y="13.8">12</text><text class="year-no" x="211" y="26">13</text><text class="year-no" x="211" y="38.2">14</text><text class="year-no" x="211" y="50.4">15</text><text class="year-no" x="211" y="62.6">16</text><text class="year-no" x="211" y="74.8">17</text><text class="year-no" x="211" y="87">18</text><text class="year-no" x="211" y="99.2">19</text><text class="year-no year-no--major" x="211" y="113.3">20</text>
    </g>
    <g class="decade" transform="translate(0,335.8)">
      <rect x="226" y="-4" width="321.1" height="122" fill="url(#week-cell)"/><rect x="571.8" y="-4" width="321.1" height="122" fill="url(#week-cell)"/>
      <text class="year-no" x="211" y="1.6">21</text><text class="year-no" x="211" y="13.8">22</text><text class="year-no" x="211" y="26">23</text><text class="year-no" x="211" y="38.2">24</text><text class="year-no" x="211" y="50.4">25</text><text class="year-no" x="211" y="62.6">26</text><text class="year-no" x="211" y="74.8">27</text><text class="year-no" x="211" y="87">28</text><text class="year-no" x="211" y="99.2">29</text><text class="year-no year-no--major" x="211" y="113.3">30</text>
    </g>
    <g class="decade" transform="translate(0,470.2)">
      <rect x="226" y="-4" width="321.1" height="122" fill="url(#week-cell)"/><rect x="571.8" y="-4" width="321.1" height="122" fill="url(#week-cell)"/>
      <text class="year-no" x="211" y="1.6">31</text><text class="year-no" x="211" y="13.8">32</text><text class="year-no" x="211" y="26">33</text><text class="year-no" x="211" y="38.2">34</text><text class="year-no" x="211" y="50.4">35</text><text class="year-no" x="211" y="62.6">36</text><text class="year-no" x="211" y="74.8">37</text><text class="year-no" x="211" y="87">38</text><text class="year-no" x="211" y="99.2">39</text><text class="year-no year-no--major" x="211" y="113.3">40</text>
    </g>
    <g class="decade" transform="translate(0,604.6)">
      <rect x="226" y="-4" width="321.1" height="122" fill="url(#week-cell)"/><rect x="571.8" y="-4" width="321.1" height="122" fill="url(#week-cell)"/>
      <text class="year-no" x="211" y="1.6">41</text><text class="year-no" x="211" y="13.8">42</text><text class="year-no" x="211" y="26">43</text><text class="year-no" x="211" y="38.2">44</text><text class="year-no" x="211" y="50.4">45</text><text class="year-no" x="211" y="62.6">46</text><text class="year-no" x="211" y="74.8">47</text><text class="year-no" x="211" y="87">48</text><text class="year-no" x="211" y="99.2">49</text><text class="year-no year-no--major" x="211" y="113.3">50</text>
    </g>
    <g class="decade" transform="translate(0,739)">
      <rect x="226" y="-4" width="321.1" height="122" fill="url(#week-cell)"/><rect x="571.8" y="-4" width="321.1" height="122" fill="url(#week-cell)"/>
      <text class="year-no" x="211" y="1.6">51</text><text class="year-no" x="211" y="13.8">52</text><text class="year-no" x="211" y="26">53</text><text class="year-no" x="211" y="38.2">54</text><text class="year-no" x="211" y="50.4">55</text><text class="year-no" x="211" y="62.6">56</text><text class="year-no" x="211" y="74.8">57</text><text class="year-no" x="211" y="87">58</text><text class="year-no" x="211" y="99.2">59</text><text class="year-no year-no--major" x="211" y="113.3">60</text>
    </g>
    <g class="decade" transform="translate(0,873.4)">
      <rect x="226" y="-4" width="321.1" height="122" fill="url(#week-cell)"/><rect x="571.8" y="-4" width="321.1" height="122" fill="url(#week-cell)"/>
      <text class="year-no" x="211" y="1.6">61</text><text class="year-no" x="211" y="13.8">62</text><text class="year-no" x="211" y="26">63</text><text class="year-no" x="211" y="38.2">64</text><text class="year-no" x="211" y="50.4">65</text><text class="year-no" x="211" y="62.6">66</text><text class="year-no" x="211" y="74.8">67</text><text class="year-no" x="211" y="87">68</text><text class="year-no" x="211" y="99.2">69</text><text class="year-no year-no--major" x="211" y="113.3">70</text>
    </g>
    <g class="decade" transform="translate(0,1007.8)">
      <rect x="226" y="-4" width="321.1" height="122" fill="url(#week-cell)"/><rect x="571.8" y="-4" width="321.1" height="122" fill="url(#week-cell)"/>
      <text class="year-no" x="211" y="1.6">71</text><text class="year-no" x="211" y="13.8">72</text><text class="year-no" x="211" y="26">73</text><text class="year-no" x="211" y="38.2">74</text><text class="year-no" x="211" y="50.4">75</text><text class="year-no" x="211" y="62.6">76</text><text class="year-no" x="211" y="74.8">77</text><text class="year-no" x="211" y="87">78</text><text class="year-no" x="211" y="99.2">79</text><text class="year-no year-no--major" x="211" y="113.3">80</text>
    </g>
  </svg>

  <p class="quote">Life can only be understood backwards; but it must be lived forwards.”</p>
  <p class="quote__author">— Anselm Brodtvik</p>
</main>
</body>
</html>
```